R T Security Flyer - Security Based Company

Security company offering installation of CCTV and Intruder alarm systems mainly but not limited to home alarms. Feel free to be creative

Target Market(s)

Residential and Commercial properties, Facility Managers, local business

Requirements
Must have
• smart professional finish, logo and latest up to date pictures if on kit

```html
<!DOCTYPE html>
<html lang="en">
<head>
<meta charset="utf-8">
<title>R T Security Flyers</title>
<link href="https://fonts.googleapis.com/css2?family=Roboto:wght@300;400;500;700&family=Roboto+Condensed:wght@400;700&display=swap" rel="stylesheet">
<style>
  :root {
    --orange: #f05a1e;
    --ink: #3a3a3a;
    --muted: #5d5d5d;
    --paper: #ffffff;
    --backdrop: #eceff1;
    --badge-blue: #2e5da8;
  }
  * { box-sizing: border-box; margin: 0; padding: 0; }
  html, body { width: 889px; height: 1200px; overflow: hidden; background: var(--backdrop); }
  body { font-family: "Roboto", sans-serif; color: var(--ink); position: relative; }

  .page {
    position: absolute; top: 294px; width: 432px; height: 611px;
    background: var(--paper); overflow: hidden;
    box-shadow: 0 2px 8px rgba(0,0,0,0.18);
  }
  .page-services { left: 8px; }
  .page-cloud { left: 449px; }

  .hero { position: absolute; top: 0; left: 0; }
  .hero svg { display: block; }

  .brand { position: absolute; left: 0; width: 100%; display: flex; flex-direction: column; align-items: center; }
  .brand-mark { width: 30px; height: 30px; border: 3px solid var(--orange); margin-bottom: 6px; }
  .brand-name {
    font-family: "Roboto Condensed", sans-serif; font-weight: 700;
    font-size: 18px; color: var(--orange); letter-spacing: 0.5px; text-transform: uppercase; line-height: 1;
  }

  .tick-list { list-style: none; }
  .tick-list li { position: relative; padding-left: 14px; font-weight: 300; color: var(--muted); }
  .tick-list li::before {
    content: ""; position: absolute; left: 0; width: 8px; height: 8px;
    border-radius: 50%; background: var(--orange);
  }
  .tick-list li::after {
    content: ""; position: absolute; left: 2px; width: 4px; height: 2px;
    border-left: 1px solid #fff; border-bottom: 1px solid #fff; transform: rotate(-45deg);
  }

  /* Services flyer */
  .page-services .brand { top: 258px; }
  .headline { position: absolute; top: 348px; width: 100%; text-align: center; text-transform: uppercase; font-family: "Roboto Condensed", sans-serif; font-size: 18px; line-height: 1.2; }
  .headline .line1 { font-weight: 700; color: var(--orange); }
  .headline .line2 { font-weight: 400; color: var(--ink); }
  .headline .line2 strong { color: var(--orange); font-weight: 700; }

  .services { position: absolute; top: 410px; left: 12px; right: 12px; display: grid; grid-template-columns: 1fr 1fr; column-gap: 14px; }
  .services li { font-size: 6.6px; line-height: 1.75; margin-bottom: 7px; text-align: justify; }
  .services li::before { top: 2px; }
  .services li::after { top: 4px; }

  .cta-band {
    position: absolute; top: 525px; left: 0; right: 0; height: 30px;
    background: var(--orange); color: #fff; text-align: center;
    font-size: 7.6px; line-height: 1.5; padding-top: 4px;
  }

  .footer { position: absolute; top: 565px; left: 10px; right: 10px; height: 36px; display: flex; align-items: center; gap: 8px; font-size: 6.4px; color: var(--muted); }
  .footer .item { display: flex; align-items: center; gap: 4px; line-height: 1.45; }
  .footer .divider { width: 1px; height: 26px; background: var(--orange); }
  .footer .email { font-size: 5.4px; }
  .footer .accent { color: var(--orange); }
  .badge-round { width: 26px; height: 26px; border-radius: 50%; border: 2px solid var(--badge-blue); background: #e9eef7; margin-left: auto; }
  .badge-listing { width: 74px; height: 16px; border-radius: 3px; background: var(--orange); }

  /* Cloud flyer */
  .page-cloud .brand { top: 210px; }
  .intro { position: absolute; top: 298px; left: 18px; right: 14px; font-family: "Roboto Condensed", sans-serif; font-size: 11.4px; line-height: 1.35; text-transform: uppercase; color: var(--ink); }
  .intro .accent { color: var(--orange); font-weight: 700; }
  .benefits-title { position: absolute; top: 356px; left: 18px; font-family: "Roboto Condensed", sans-serif; text-transform: uppercase; line-height: 1.05; }
  .benefits-title .small { font-size: 14px; color: var(--ink); }
  .benefits-title .big { font-size: 23px; font-weight: 700; color: var(--orange); }
  .devices { position: absolute; top: 360px; left: 278px; width: 130px; height: 66px; border-radius: 4px; background: linear-gradient(135deg, #cfd4da, #2a73b8); }
  .benefits { position: absolute; top: 408px; left: 18px; width: 250px; }
  .benefits li { font-size: 5.8px; line-height: 1.35; margin-bottom: 6px; color: var(--ink); font-weight: 400; }
  .benefits li::before { top: 0; width: 7px; height: 7px; }
  .benefits li::after { top: 1.5px; left: 1.5px; }
  .house { position: absolute; top: 446px; left: 282px; width: 135px; height: 110px; border-radius: 4px; background: linear-gradient(135deg, #e8ecef, #9fb7a0); }
  .about { position: absolute; top: 522px; left: 18px; width: 250px; font-size: 5.6px; line-height: 1.45; color: var(--ink); text-align: justify; }
  .signoff { position: absolute; top: 574px; left: 18px; font-size: 7px; line-height: 1.4; color: var(--ink); }
  .signoff .accent { color: var(--orange); font-weight: 500; }
  .partner { position: absolute; top: 572px; right: 22px; display: flex; align-items: center; gap: 4px; font-size: 10px; font-weight: 700; color: #2b3a67; }
  .partner .dot { width: 9px; height: 9px; border-radius: 50%; background: #2b3a67; }
</style>
</head>
<body>

  <article class="page page-services">
    <header class="hero">
      <svg width="432" height="330" viewBox="0 0 432 330">
        <defs>
          <linearGradient id="servicesTone" x1="0" y1="0" x2="1" y2="1">
            <stop offset="0" stop-color="#9aa0a5"/>
            <stop offset="0.5" stop-color="#eef0f0"/>
            <stop offset="1" stop-color="#4a5258"/>
          </linearGradient>
        </defs>
        <rect width="432" height="330" fill="url(#servicesTone)" role="img"
              aria-label="Photograph of a wall-mounted CCTV camera and a hand holding a smartphone with a home security app, in front of a modern white house"/>
        <path d="M0,226 C80,250 160,290 270,268 C340,252 390,236 432,238 L432,330 L0,330 Z" fill="var(--orange)"/>
        <path d="M0,302 C110,302 210,252 310,262 C370,268 405,276 432,276 L432,330 L0,330 Z" fill="var(--paper)"/>
      </svg>
    </header>

    <div class="brand">
      <div class="brand-mark"></div>
      <div class="brand-name">R T Security</div>
    </div>

    <h1 class="headline">
      <div class="line1">Are you looking</div>
      <div class="line2">to keep you or your <strong>premises safe?</strong></div>
    </h1>

    <section class="services">
      <ul class="tick-list">
        <li>We install, maintain and repair all intruder alarms, CCTV, intercom and access control</li>
        <li>View, control and manage your security systems anywhere in the world with smartphone apps</li>
        <li>Feel at ease with monitoring services and police response tailored to suit you and your business</li>
      </ul>
      <ul class="tick-list">
        <li>We can takeover any existing security system and offer maintenance checks to guarantee the best performance for you and your premises</li>
        <li>We understand that being security conscious is ever increasing, protecting your property and family is a number one priority</li>
        <li>Our fully insured and accredited team offer quality, safety and cost efficiency throughout and whole process</li>
      </ul>
    </section>

    <div class="cta-band">
      If you are looking to improve the security in your home, office or commercial property<br>
      then call a member of our team today for a free quote.
    </div>

    <footer class="footer">
      <div class="item">
        <svg width="7" height="10" viewBox="0 0 14 20"><path d="M7,0 C3,0 0,3 0,7 C0,12 7,20 7,20 C7,20 14,12 14,7 C14,3 11,0 7,0 Z" fill="var(--orange)"/><circle cx="7" cy="7" r="2.6" fill="#fff"/></svg>
        <span>14 Maple Road, Harlow,<br>Essex, CM18 2PL</span>
      </div>
      <div class="divider"></div>
      <div class="item">
        <span>www.<span class="accent">rtsecuritysystems</span>.co.uk<br><span class="email">operations@<span class="accent">rtsecuritysystems</span>.co.uk</span></span>
      </div>
      <div class="divider"></div>
      <div class="item">
        <svg width="8" height="8" viewBox="0 0 24 24"><path d="M6.6,10.8 C8,13.6 10.4,16 13.2,17.4 L15.4,15.2 C15.7,14.9 16.1,14.8 16.4,15 C17.5,15.4 18.7,15.6 20,15.6 C20.6,15.6 21,16 21,16.6 L21,20 C21,20.6 20.6,21 20,21 C10.6,21 3,13.4 3,4 C3,3.4 3.4,3 4,3 L7.5,3 C8.1,3 8.5,3.4 8.5,4 C8.5,5.3 8.7,6.5 9.1,7.6 C9.2,7.9 9.1,8.3 8.9,8.6 Z" fill="var(--orange)"/></svg>
        <span>01632 960481</span>
      </div>
      <div class="badge-round"></div>
      <div class="badge-listing"></div>
    </footer>
  </article>

  <article class="page page-cloud">
    <header class="hero">
      <svg width="432" height="290" viewBox="0 0 432 290">
        <defs>
          <linearGradient id="cityTone" x1="0" y1="0" x2="0" y2="1">
            <stop offset="0" stop-color="#3f6fa8"/>
            <stop offset="0.55" stop-color="#6b7f92"/>
            <stop offset="1" stop-color="#2d3a4a"/>
          </linearGradient>
        </defs>
        <rect width="432" height="290" fill="url(#cityTone)" role="img"
              aria-label="Evening photograph of a domed cathedral and a pedestrian bridge over a river in a city"/>
        <path d="M0,160 C60,170 110,230 200,228 C290,226 340,175 432,180 L432,290 L0,290 Z" fill="var(--orange)"/>
        <path d="M0,232 C90,235 150,170 250,180 C340,188 390,258 432,262 L432,290 L0,290 Z" fill="var(--paper)"/>
      </svg>
    </header>

    <div class="brand">
      <div class="brand-mark"></div>
      <div class="brand-name">R T Security</div>
    </div>

    <p class="intro">
      <span class="accent">R T Security Systems</span><br>
      are using the latest <strong>cloud-based technology</strong> to stay<br>
      connected with your home and <span class="accent">business 24/7.</span>
    </p>

    <h2 class="benefits-title">
      <div class="small">Some benefits of</div>
      <div class="big">Cloud services are</div>
    </h2>

    <div class="devices" role="img" aria-label="Photograph of an alarm keypad and two smartphones showing the security app"></div>

    <ul class="tick-list benefits">
      <li>High level support 24/7</li>
      <li>Reduce engineer call outs and running costs</li>
      <li>Identify issues in advance</li>
      <li>Remotely manage systems to ensure correct operation</li>
      <li>Remote health checks carried out to keep your system performing as it should</li>
      <li>Automatically update your system with the latest releases<br>via cloud application software</li>
      <li>Interact, control and integrate your security system like never before</li>
    </ul>

    <div class="house" role="img" aria-label="Illustration of a cut-away house with connected security sensors"></div>

    <p class="about">
      With the new cloud-based system we can check the alarm performance anytime you need it. This gives us the capability to assist you in any of your needs, be that changing user codes or system configuration. We are always there, working in the background to make sure you have the support and help you need. This is taking alarm systems into the future and leaving the stand-alone systems in the past.
    </p>

    <p class="signoff">
      <span class="accent">R T Security Systems</span><br>
      are always there, always available, wherever and whenever you need us
    </p>

    <div class="partner"><span class="dot"></span>Norvane</div>
  </article>

</body>
</html>
```